PowerPoint Design Project

We need a powerpoint design for our consulting company, Brindle Consulting. We provide technology strategy and solutioning services, with an emphasis on cloud technology. More information about our services can be found at www.brindleconsulting-example.com

We are looking for a design that is professional, but not corporate stuffy. The design needs to use our primary colors in our brand.
Updates

Reason: We need to iterate on some of the great designs, plus, many people have not had a chance to submit their design yet.

Reason: We had a lot of people accept the project, but not all of them have responded yet. We wanted to get them some time, plus, ask a couple of people to make some minor revisions.

Target Market(s)

Technology buyers between the ages of 30-55 at Vantor 1000 companies

Industry/Entity Type

It Company

Requirements
Must have
• Must follow our logo colors.
Must have at least a cover slide and interior content slide.
Should not have
• Should not contain anything cartoonish or anything with lots of clouds

```html
<!DOCTYPE html>
<html lang="en">
<head>
<meta charset="utf-8">
<title>Brindle Consulting – Slide Templates</title>
<link rel="stylesheet" href="https://fonts.googleapis.com/css2?family=Open+Sans:wght@400;600;700&display=swap">
<style>
  :root {
    --board-light: #f4f4f4;
    --board-dark: #c9c9c9;
    --navy: #2c3f59;
    --blue-glow: #3f70a8;
    --teal: #3fb3c9;
    --panel-grey: #c8c8c8;
    --curve-grey: #d6d6d6;
    --ink: #2a3a52;
    --muted: #9aa7b8;
    --label: #b9c3d0;
    --social: #4a86c5;
    --white: #ffffff;
  }
  * { margin: 0; padding: 0; box-sizing: border-box; }
  html, body { width: 1200px; height: 1000px; overflow: hidden; }
  body {
    font-family: "Open Sans", sans-serif;
    background: radial-gradient(ellipse at 50% 45%, var(--board-light) 0%, var(--board-dark) 100%);
    position: relative;
  }
  .slide {
    position: absolute;
    left: 388px;
    width: 420px;
    height: 295px;
    overflow: hidden;
  }
  .brand-line { display: flex; align-items: center; gap: 7px; white-space: nowrap; }
  .brand-dot { border-radius: 50%; background: var(--teal); flex: none; }
  .brand-name { color: var(--white); font-weight: 600; }

  /* Cover slide */
  .slide--cover { top: 26px; background: radial-gradient(ellipse 190px 150px at 50% 32%, var(--blue-glow) 0%, var(--navy) 100%); }
  .cover-curve { position: absolute; left: 0; top: 0; width: 420px; height: 295px; }
  .cover-brand {
    position: absolute; left: 0; right: 0; top: 136px;
    display: flex; flex-direction: column; align-items: center;
  }
  .cover-brand .brand-dot { width: 11px; height: 11px; }
  .cover-brand .brand-name { font-size: 22px; letter-spacing: -0.2px; }
  .cover-brand .tagline { color: var(--teal); font-size: 8px; font-weight: 600; align-self: flex-end; margin-right: 88px; margin-top: -1px; }
  .cover-url {
    position: absolute; left: 0; right: 0; bottom: 11px;
    text-align: center; color: var(--ink); font-size: 11.5px; font-weight: 600; letter-spacing: 0.2px;
  }

  /* Interior slide */
  .slide--interior { top: 340px; background: var(--panel-grey); border-top: 6px solid var(--navy); }
  .interior-footer {
    position: absolute; left: 0; right: 0; bottom: 0; height: 24px;
    background: var(--navy);
    display: flex; align-items: center; justify-content: space-between; padding: 0 14px 0 9px;
  }
  .interior-footer .brand-line { gap: 4px; }
  .interior-footer .brand-dot { width: 6px; height: 6px; }
  .interior-footer .brand-name { font-size: 9.5px; }
  .footer-url { color: var(--white); font-size: 9px; font-weight: 600; }

  /* Closing slide */
  .slide--closing { top: 658px; background: var(--navy); }
  .closing-brand {
    position: absolute; left: 0; right: 0; top: 143px;
    display: flex; flex-direction: column; align-items: center;
  }
  .closing-brand .brand-line { gap: 4px; }
  .closing-brand .brand-dot { width: 6px; height: 6px; }
  .closing-brand .brand-name { font-size: 10px; }
  .closing-brand .tagline { color: var(--muted); font-size: 4.5px; margin-left: 30px; }
  .offices { position: absolute; left: 12px; bottom: 11px; font-size: 6px; line-height: 7px; color: var(--muted); }
  .office + .office { margin-top: 5px; }
  .office-name { font-weight: 700; color: var(--label); }
  .closing-contact {
    position: absolute; right: 10px; bottom: 13px;
    display: flex; align-items: center; gap: 3px; font-size: 5.5px; color: var(--muted);
  }
  .closing-contact .social { width: 10px; height: 10px; border-radius: 50%; background: var(--social); }
  .closing-contact .url { margin-right: 6px; }
</style>
</head>
<body>
  <section class="slide slide--cover">
    <svg class="cover-curve" viewBox="0 0 420 295" aria-hidden="true">
      <defs>
        <linearGradient id="curveShade" x1="0" y1="0" x2="0" y2="1">
          <stop offset="0" stop-color="#000" stop-opacity="0.35"/>
          <stop offset="1" stop-color="#000" stop-opacity="0"/>
        </linearGradient>
      </defs>
      <path d="M0 270 Q210 250 420 270 L420 280 Q210 260 0 280 Z" fill="url(#curveShade)"/>
      <path d="M0 272 Q210 252 420 272 L420 295 L0 295 Z" fill="var(--curve-grey)"/>
    </svg>
    <div class="cover-brand">
      <div class="brand-line"><span class="brand-dot"></span><span class="brand-name">Brindle Consulting</span></div>
      <div class="tagline">strategy + cloud + delivery</div>
    </div>
    <div class="cover-url">www.brindleconsulting-example.com</div>
  </section>

  <section class="slide slide--interior">
    <footer class="interior-footer">
      <div class="brand-line"><span class="brand-dot"></span><span class="brand-name">Brindle Consulting</span></div>
      <div class="footer-url">www.brindleconsulting-example.com</div>
    </footer>
  </section>

  <section class="slide slide--closing">
    <div class="closing-brand">
      <div class="brand-line"><span class="brand-dot"></span><span class="brand-name">Brindle Consulting</span></div>
      <div class="tagline">strategy + cloud + delivery</div>
    </div>
    <div class="offices">
      <div class="office"><div class="office-name">Raleigh Office</div><div>410 Pinecrest Blvd</div><div>Raleigh, NC 27615</div></div>
      <div class="office"><div class="office-name">Columbus Office</div><div>92 Harlow Lane</div><div>Columbus, OH 43215</div></div>
    </div>
    <div class="closing-contact">
      <span class="url">www.brindleconsulting-example.com</span>
      <span class="social"></span><span class="social"></span><span class="social"></span>
    </div>
  </section>
</body>
</html>
```